Brightvantage.com tech company website

Current site is www.brightvantage.com. The site will tell you about our company.

Designs we like are:
http://megainfo.quellorix.com
www.trelvo.com
www.morvasket.com

Target Market(s)

B2B

Industry/Entity Type

It Company

Coding

Coded - Design and coding required

Number of Pages Required

5+ page

Requirements
Must have
• We want to entice without giving away too much info. We like graphics and colors. But website must look official and credible.

```html
<!DOCTYPE html>
<html lang="en">
<head>
<meta charset="utf-8">
<title>Brightvantage</title>
<link rel="stylesheet" href="https://fonts.googleapis.com/css2?family=Open+Sans:wght@400;600;700;800&display=swap">
<style>
:root{
  --blue:#1f6fb6;
  --blue-dark:#185a94;
  --navy:#1d2f44;
  --ink:#2f3a45;
  --muted:#7b8690;
  --rule:#dfe3e7;
  --pale:#eef1f4;
  --footer:#2b2d30;
  --white:#fff;
}
*{box-sizing:border-box;margin:0;padding:0}
html,body{width:1200px;height:2304px;overflow:hidden}
body{font-family:"Open Sans",Arial,sans-serif;color:var(--ink);background:var(--white);position:relative}
a{color:inherit;text-decoration:none}

/* header */
.site-header{position:absolute;top:0;left:0;width:1200px;height:64px;background:var(--white);border-bottom:1px solid var(--rule)}
.brand{position:absolute;left:126px;top:14px;display:flex;align-items:center;gap:10px;font-weight:800;font-size:24px;color:var(--navy);letter-spacing:.5px}
.brand-mark{width:30px;height:30px;border-radius:50%;background:var(--blue)}
.topbar{position:absolute;right:128px;top:6px;display:flex;align-items:center;gap:16px;font-size:11px;color:var(--muted)}
.topbar .item{display:flex;align-items:center;gap:5px}
.social{display:flex;gap:4px}
.social span{width:16px;height:16px;background:#8a939b;display:block}
.main-nav{position:absolute;right:128px;top:34px;display:flex;gap:22px;font-size:11.5px;font-weight:600;color:var(--ink)}
.main-nav a.active{color:var(--blue);border-bottom:2px solid var(--blue);padding-bottom:4px}

/* hero */
.hero{position:absolute;top:64px;left:0;width:1200px;height:476px;background:linear-gradient(110deg,#1d2733 0%,#34404d 45%,#6f7a86 75%,#a8b4bf 100%)}
.hero-copy{position:absolute;left:130px;top:210px;color:var(--white);font-size:19px;font-weight:800;line-height:28px;text-transform:uppercase;letter-spacing:.3px}
.hero-dots{position:absolute;left:134px;top:436px;display:flex;gap:6px}
.hero-dots span{width:8px;height:8px;border-radius:50%;background:rgba(255,255,255,.5)}
.hero-dots span:first-child{background:var(--white)}

/* welcome */
.welcome{position:absolute;top:540px;left:0;width:1200px;height:340px}
.welcome-text{position:absolute;left:130px;top:18px;width:560px}
.welcome-text h1{font-size:22px;font-weight:800;color:var(--navy);text-transform:uppercase;margin-bottom:14px}
.welcome-text h1 em{font-style:normal;color:var(--blue)}
.welcome-text p{font-size:11.5px;line-height:19px;color:var(--muted);margin-bottom:14px}
.btn{display:inline-block;background:var(--blue);color:var(--white);font-size:11px;font-weight:700;padding:8px 14px;text-transform:uppercase}
.video-box{position:absolute;left:736px;top:-44px;width:330px;background:var(--white);box-shadow:0 2px 8px rgba(0,0,0,.2)}
.video-box h2{font-size:20px;font-weight:800;color:var(--navy);padding:10px 14px;text-transform:uppercase}
.video-box h2 em{font-style:normal;color:var(--blue)}
.video-frame{position:relative;height:196px;margin:0 8px 8px;background:linear-gradient(135deg,#c9d3dc,#7d8b99)}
.video-frame svg{position:absolute;left:131px;top:64px}
.video-bar{position:absolute;left:0;right:0;bottom:0;height:18px;background:rgba(0,0,0,.6)}

/* services */
.section-title{display:flex;align-items:center;gap:18px;font-size:15px;font-weight:800;color:var(--navy);text-transform:uppercase;justify-content:center}
.section-title::before,.section-title::after{content:"";flex:1;height:1px;background:var(--rule)}
.services{position:absolute;top:890px;left:130px;width:940px;height:520px}
.service-grid{display:grid;grid-template-columns:repeat(4,1fr);row-gap:46px;margin-top:34px}
.service{text-align:center;padding:0 20px}
.service-icon{width:66px;height:66px;border-radius:50%;background:var(--navy);margin:0 auto 12px;display:flex;align-items:center;justify-content:center;border:4px solid #d5dde5}
.service h3{font-size:12.5px;font-weight:700;color:var(--navy);margin-bottom:6px}
.service p{font-size:10.5px;line-height:16px;color:var(--muted);margin-bottom:8px}
.more{font-size:10px;font-weight:700;color:var(--navy);display:block;border-bottom:1px solid var(--rule);padding-bottom:6px;text-transform:uppercase}
.divider{position:absolute;top:1412px;left:130px;width:940px;height:1px;background:var(--rule)}

/* case studies */
.case-studies{position:absolute;top:1420px;left:0;width:1200px;height:440px;background:var(--pale);padding:28px 130px 0}
.case-grid{display:grid;grid-template-columns:repeat(3,1fr);gap:40px;margin-top:26px;padding:0 10px}
.case-image{height:160px;border:4px solid var(--white);box-shadow:0 1px 3px rgba(0,0,0,.15)}
.case-1{background:linear-gradient(135deg,#8fa7bd,#3d5a76)}
.case-2{background:linear-gradient(135deg,#5d6670,#1f2a35)}
.case-3{background:linear-gradient(135deg,#e4ecf3,#9fb7cc)}
.case h3{font-size:13px;font-weight:700;color:var(--navy);margin:14px 0 6px}
.case p{font-size:10.5px;line-height:16px;color:var(--muted);margin-bottom:6px}
.case .read{font-size:10.5px;font-weight:700;color:var(--blue)}

/* call to action */
.cta{position:absolute;top:1860px;left:0;width:1200px;height:52px;display:flex}
.cta-left{width:600px;background:var(--white);display:flex;align-items:center;justify-content:flex-end;gap:10px;padding-right:20px;font-size:14px;font-weight:800;color:var(--navy);text-transform:uppercase}
.cta-right{flex:1;background:var(--blue);display:flex;align-items:center;justify-content:space-between;padding:0 130px 0 24px;color:var(--white);font-size:15px;font-weight:800;text-transform:uppercase}
.cta-right .social span{background:var(--white);width:20px;height:20px;opacity:.9}

/* offices */
.offices{position:absolute;top:1912px;left:0;width:1200px;height:304px;background:linear-gradient(180deg,#d9ddd8,#c3c9c3)}
.office{position:absolute;top:54px;width:170px}
.office-photo{height:140px;border:3px solid var(--white);box-shadow:0 2px 6px rgba(0,0,0,.25)}
.office-label{display:flex;align-items:center;gap:6px;background:var(--blue);color:var(--white);font-size:12px;font-weight:700;text-transform:uppercase;padding:6px 8px}
.p1{background:linear-gradient(180deg,#9cc3e2,#4b7fa4)}
.p2{background:linear-gradient(180deg,#a9c1d6,#6f8596)}
.p3{background:linear-gradient(180deg,#7f98b3,#34465c)}
.p4{background:linear-gradient(180deg,#c2a478,#6b4f3a)}

/* footer */
.site-footer{position:absolute;top:2216px;left:0;width:1200px;height:88px;background:var(--footer);color:#b9bec3;font-size:11px;display:flex;align-items:center;justify-content:space-between;padding:0 130px}
.footer-nav{display:flex;gap:22px}
</style>
</head>
<body>

<header class="site-header">
  <a class="brand" href="#"><span class="brand-mark"></span>BRIGHTVANTAGE</a>
  <div class="topbar">
    <span class="item"><svg width="11" height="11" viewBox="0 0 24 24"><path fill="#7b8690" d="M6.6 10.8a15 15 0 0 0 6.6 6.6l2.2-2.2c.3-.3.7-.4 1-.2 1.1.4 2.3.6 3.6.6.6 0 1 .4 1 1V20c0 .6-.4 1-1 1A17 17 0 0 1 3 4c0-.6.4-1 1-1h3.5c.6 0 1 .4 1 1 0 1.3.2 2.5.6 3.6.1.3 0 .7-.2 1z"/></svg>555-014-2290</span>
    <span class="item"><svg width="12" height="10" viewBox="0 0 24 18"><rect x="1" y="1" width="22" height="16" fill="none" stroke="#7b8690" stroke-width="2"/><path d="M1 1l11 9 11-9" fill="none" stroke="#7b8690" stroke-width="2"/></svg>info@brightvantage.com</span>
    <span class="social"><span></span><span></span><span></span><span></span></span>
  </div>
  <nav class="main-nav">
    <a class="active" href="#">Home</a><a href="#">About</a><a href="#">Big Data &amp; Analytics</a><a href="#">Perception &amp; Influence</a><a href="#">Case Studies</a><a href="#">Contact</a>
  </nav>
</header>

<section class="hero" role="img" aria-label="Hand arranging puzzle pieces beside a rising 3D bar chart">
  <p class="hero-copy">We optimize our clients outcomes<br>through data intelligence gathering,<br>analytics, situation monitoring,<br>content development and active<br>information</p>
  <div class="hero-dots"><span></span><span></span><span></span></div>
</section>

<section class="welcome">
  <div class="welcome-text">
    <h1>Welcome to <em>Bright</em>vantage</h1>
    <p>We help business leaders turn scattered data into clear decisions. Our analysts gather, sort and read signals from every channel so your teams can act faster, spend smarter and reach the buyers that matter most to growth.</p>
    <p>From social listening to content planning, each service links into one view of your market, built for steady and measured results.</p>
    <a class="btn" href="#">Read More</a>
  </div>
  <aside class="video-box">
    <h2>Latest <em>Video</em></h2>
    <div class="video-frame" role="img" aria-label="Video still of a presenter pointing at a screen">
      <svg width="52" height="38" viewBox="0 0 52 38"><rect width="52" height="38" rx="8" fill="#2b3440"/><path d="M20 11l14 8-14 8z" fill="#fff"/></svg>
      <div class="video-bar"></div>
    </div>
  </aside>
</section>

<section class="services">
  <h2 class="section-title">Our Services</h2>
  <div class="service-grid">
    <div class="service"><div class="service-icon"><svg width="30" height="30" viewBox="0 0 30 30"><circle cx="15" cy="15" r="12" fill="none" stroke="#fff" stroke-width="2"/><circle cx="15" cy="15" r="7" fill="none" stroke="#fff" stroke-width="2"/><circle cx="15" cy="15" r="2.5" fill="#fff"/></svg></div><h3>Truly Targeted Marketing</h3><p>Short note on how this service lifts your results.</p><a class="more" href="#">More</a></div>
    <div class="service"><div class="service-icon"><svg width="30" height="30" viewBox="0 0 30 30"><circle cx="15" cy="10" r="5" fill="#fff"/><path d="M5 26c0-6 4-9 10-9s10 3 10 9z" fill="#fff"/></svg></div><h3>Lead Generation</h3><p>Short note on how this service lifts your results.</p><a class="more" href="#">More</a></div>
    <div class="service"><div class="service-icon"><svg width="30" height="30" viewBox="0 0 30 30"><rect x="5" y="16" width="5" height="10" fill="#fff"/><rect x="12.5" y="10" width="5" height="16" fill="#fff"/><rect x="20" y="4" width="5" height="22" fill="#fff"/></svg></div><h3>Data Enhancement</h3><p>Short note on how this service lifts your results.</p><a class="more" href="#">More</a></div>
    <div class="service"><div class="service-icon"><svg width="30" height="30" viewBox="0 0 30 30"><circle cx="15" cy="15" r="11" fill="none" stroke="#fff" stroke-width="2"/><path d="M15 8v14M11 12h6a2 2 0 0 1 0 4h-4a2 2 0 0 0 0 4h6" fill="none" stroke="#fff" stroke-width="2"/></svg></div><h3>Data Monetization</h3><p>Short note on how this service lifts your results.</p><a class="more" href="#">More</a></div>
    <div class="service"><div class="service-icon"><svg width="30" height="30" viewBox="0 0 30 30"><circle cx="15" cy="8" r="4" fill="#fff"/><circle cx="6" cy="20" r="3.5" fill="#fff"/><circle cx="24" cy="20" r="3.5" fill="#fff"/><path d="M15 12L6 20M15 12l9 8" stroke="#fff" stroke-width="2"/></svg></div><h3>Influencer Identification</h3><p>Short note on how this service lifts your results.</p><a class="more" href="#">More</a></div>
    <div class="service"><div class="service-icon"><svg width="30" height="30" viewBox="0 0 30 30"><path d="M4 24l7-8 5 4 10-12" fill="none" stroke="#fff" stroke-width="2.5"/><path d="M21 8h5v5" fill="none" stroke="#fff" stroke-width="2.5"/></svg></div><h3>Business Intelligence</h3><p>Short note on how this service lifts your results.</p><a class="more" href="#">More</a></div>
    <div class="service"><div class="service-icon"><svg width="30" height="30" viewBox="0 0 30 30"><path d="M15 3l3.5 7.5 8 1-6 5.5 1.6 8L15 21l-7.1 4 1.6-8-6-5.5 8-1z" fill="#fff"/></svg></div><h3>Competitive Advantage</h3><p>Short note on how this service lifts your results.</p><a class="more" href="#">More</a></div>
    <div class="service"><div class="service-icon"><svg width="30" height="30" viewBox="0 0 30 30"><path d="M6 12a9 9 0 0 1 16-4M24 18a9 9 0 0 1-16 4" fill="none" stroke="#fff" stroke-width="2.5"/><path d="M22 3v6h-6M8 27v-6h6" fill="none" stroke="#fff" stroke-width="2.5"/></svg></div><h3>Campaign Synchronization</h3><p>Short note on how this service lifts your results.</p><a class="more" href="#">More</a></div>
  </div>
</section>
<div class="divider"></div>

<section class="case-studies">
  <h2 class="section-title">Case Studies</h2>
  <div class="case-grid">
    <article class="case"><div class="case-image case-1" role="img" aria-label="Hands reviewing charts on a desk"></div><h3>Maintained share value for fortune...</h3><p>A short summary of the project goals and the outcome we delivered for the client.</p><a class="read" href="#">Read More</a></article>
    <article class="case"><div class="case-image case-2" role="img" aria-label="Tablet showing a financial dashboard"></div><h3>Initial Public Offering Management...</h3><p>A short summary of the project goals and the outcome we delivered for the client.</p><a class="read" href="#">Read More</a></article>
    <article class="case"><div class="case-image case-3" role="img" aria-label="Target board with arrows and small figures"></div><h3>Increased sales with our Truly Targeting...</h3><p>A short summary of the project goals and the outcome we delivered for the client.</p><a class="read" href="#">Read More</a></article>
  </div>
</section>

<section class="cta">
  <div class="cta-left"><svg width="22" height="22" viewBox="0 0 22 22"><circle cx="11" cy="11" r="11" fill="#1f6fb6"/><path d="M9 6l5 5-5 5" fill="none" stroke="#fff" stroke-width="2"/></svg>What are you waiting for?</div>
  <div class="cta-right">Let's Talk<span class="social"><span></span><span></span><span></span><span></span></span></div>
</section>

<section class="offices" role="img" aria-label="Street map of the United States with office locations">
  <div class="office" style="left:140px"><div class="office-photo p1" role="img" aria-label="Fort Lauderdale waterfront skyline"></div><div class="office-label"><svg width="10" height="14" viewBox="0 0 10 14"><path d="M5 0a5 5 0 0 1 5 5c0 4-5 9-5 9S0 9 0 5a5 5 0 0 1 5-5z" fill="#fff"/></svg>Fort Lauderdale</div></div>
  <div class="office" style="left:380px"><div class="office-photo p2" role="img" aria-label="Capitol building in Washington DC"></div><div class="office-label"><svg width="10" height="14" viewBox="0 0 10 14"><path d="M5 0a5 5 0 0 1 5 5c0 4-5 9-5 9S0 9 0 5a5 5 0 0 1 5-5z" fill="#fff"/></svg>Washington DC</div></div>
  <div class="office" style="left:620px"><div class="office-photo p3" role="img" aria-label="New York City skyline"></div><div class="office-label"><svg width="10" height="14" viewBox="0 0 10 14"><path d="M5 0a5 5 0 0 1 5 5c0 4-5 9-5 9S0 9 0 5a5 5 0 0 1 5-5z" fill="#fff"/></svg>New York City</div></div>
  <div class="office" style="left:860px"><div class="office-photo p4" role="img" aria-label="Las Vegas strip at dusk"></div><div class="office-label"><svg width="10" height="14" viewBox="0 0 10 14"><path d="M5 0a5 5 0 0 1 5 5c0 4-5 9-5 9S0 9 0 5a5 5 0 0 1 5-5z" fill="#fff"/></svg>Las Vegas</div></div>
</section>

<footer class="site-footer">
  <span>© Copyright Brightvantage LLC 2015</span>
  <nav class="footer-nav"><a href="#">Home</a><a href="#">About</a><a href="#">Big Data &amp; Analytics</a><a href="#">Perception &amp; Influence</a><a href="#">Case Studies</a><a href="#">Contact</a></nav>
</footer>

</body>
</html>
```